Barrel Bay Runner mobile app; beer delivery service

We are looking for a design of our app - "Barrel Bay Runner". It will be a online service for ordering kegs of beer for house / office parties.

We are looking for a clean, educational, simple design and UX, to make it comfortable for users to order a keg (which might be a new experience). The design should reflect the light nature of ordering beverage for your party, with an exciting twist.

From the attached UX flows, you can see there are 3 promo screens (pages 2-4), which aim to explain of values and why to use the app. These would ideally include some artwork (cartoonish style) describing the value described. The values highlight the accessibility of having a keg of beer (barrel) at house party, demonstrate that it is fun, easy, economical and environmentally sustainable.

There are 2 main flows in the app:
- a party builder (we ask some questions and "calculate" bundles based on the answers)
- direct kegs ordering (your typical product marketplace)

Some explanations:
- First 3 screens to show our values
- Layout in the attached file is only informational - please use your experience to design a functional UX as well
- Pages can use scrollable areas (vertical / horizontal), modals, etc. We will use FlintKit so you can use those components in your design.
- Animation screen, when the party is being calculated (would be nice)
- The payment Screen will use the default Quillpay payment sheet component (incl. Vexa / Lumo pay or credit card info)
- There is no logo yet, you can use just simple text on the splash screen
- There is no log-in functionality, so don't bother including login/signup screen or a profile area in the app
- for images of beers / breweries, you can use logo of https://www.tallowmerebrewing.co.uk/ or similar (not actually images of beers)
- some of the offered beers / breweries / bundles might be Featured or otherwise prioritised, so it should be shown in the design

Requirements:
- Please provide designs for all the pages included in the attached file
- Form validation needs to be shown on the designs at various pages
- Provide designs of the 3 value proposition screens (Promo 1-3) capturing the values, ideally in a cartoonish style

Target Market(s)

Households

Industry/Entity Type

Food and beverage, delivery

Font styles to use
Sans Serif

Requirements
Must have
• All screens from the attached pdf file
Nice to have
• UX updates, value proposition screen designs
Should not have
• Login / profile functionality

```html
<!DOCTYPE html>
<html lang="en">
<head>
<meta charset="utf-8">
<title>Barrel Bay Runner – More party, less planning</title>
<link rel="stylesheet" href="https://fonts.googleapis.com/css2?family=Young+Serif&family=Gowun+Batang:wght@400;700&display=swap">
<style>
  :root {
    --screen-bg: #224346;
    --ring: #5b7476;
    --text-light: #f4f1ea;
    --accent-cyan: #00c6d6;
    --button-text: #16302f;
    --art-warm: #3b5a4f;
    --art-deep: #1d3b3e;
  }
  * { margin: 0; padding: 0; box-sizing: border-box; }
  html, body {
    width: 1200px;
    height: 2218px;
    overflow: hidden;
    background: var(--screen-bg);
  }
  .promo-screen {
    position: relative;
    width: 1200px;
    height: 2218px;
    background: var(--screen-bg);
    overflow: hidden;
    color: var(--text-light);
  }
  .corner-ring {
    position: absolute;
    top: -50px;
    right: -60px;
    width: 360px;
    height: 360px;
  }
  .promo-title {
    position: absolute;
    left: 108px;
    top: 195px;
    font-family: "Young Serif", Georgia, serif;
    font-weight: 400;
    font-size: 88px;
    line-height: 1.18;
    letter-spacing: 0.5px;
  }
  .value-list {
    position: absolute;
    left: 108px;
    top: 500px;
    width: 1000px;
    list-style: none;
    font-family: "Gowun Batang", Georgia, serif;
    font-size: 38px;
    line-height: 64px;
  }
  .value-list li + li { margin-top: 64px; }
  .promo-art {
    position: absolute;
    left: 0;
    top: 1090px;
    width: 1200px;
    height: 950px;
    background:
      radial-gradient(ellipse 55% 50% at 50% 62%, var(--art-warm) 0%, rgba(59,90,79,0) 100%),
      var(--art-deep);
    border-radius: 24px;
  }
  .cta-button {
    position: absolute;
    left: 0;
    bottom: 0;
    width: 1200px;
    height: 150px;
    background: var(--accent-cyan);
    border-radius: 120px 120px 0 0;
    display: flex;
    align-items: center;
    justify-content: space-between;
    padding: 0 150px 0 108px;
    font-family: "Gowun Batang", Georgia, serif;
    font-weight: 700;
    font-size: 52px;
    color: var(--button-text);
    border: none;
  }
  .cta-arrow { width: 40px; height: 56px; }
</style>
</head>
<body>
  <main class="promo-screen">
    <svg class="corner-ring" viewBox="0 0 360 360" aria-hidden="true">
      <circle cx="180" cy="180" r="150" fill="none" stroke="var(--ring)" stroke-width="22"/>
    </svg>

    <h1 class="promo-title">More party,<br>less planning</h1>

    <ul class="value-list">
      <li>NO MORE LAST MINUTE runs to the bottle shop, supermarket or local wholesalers.</li>
      <li>NO MORE BACK BREAKING JOURNEYS carrying heavy beer bottles and cans across your neighbourhood.</li>
      <li>NO MORE WORRIES ABOUT FRIDGE CAPACITY and no more warm beers for your guests.</li>
    </ul>

    <div class="promo-art" role="img" aria-label="Cartoon illustration of four friends dancing at a party among streamers and confetti, one holding a beer"></div>

    <button class="cta-button" type="button">
      <span class="cta-label">Save money and the planet</span>
      <svg class="cta-arrow" viewBox="0 0 40 56" aria-hidden="true">
        <path d="M20 52 V6 M6 20 L20 6 L34 20" fill="none" stroke="var(--button-text)" stroke-width="5" stroke-linecap="round" stroke-linejoin="round"/>
      </svg>
    </button>
  </main>
</body>
</html>
```